Need Help having my business card stand out

I am the owner of Pine Ridge Canine Coaching and would like for my business cards to stand out. I have been trying to keep designing them myself but I can't get what I have in my head on the card. I will try my best to post templates that I like for inspirations. I want something unique but elegant. I don't want in to look cartoony or cheesy. It needs to pop in a pet shop but also in a coffee shop or gym.

Target Market(s)

Dog owners, Married ,No young kids Jr High school kids and up (maybe kids on the way) Executives, Stay at home moms/wives, Small business owners

Industry/Entity Type

Dog Training

Contact Information for Business Card

Trevor Holloway, 555-304-7162, info@pineridgecanine.example, www.pineridgecanine.example

Colors

Designer to choose colors to be used in the design.

Requirements
Must have
• my logo
Should not have
• Cursive lettering

```html
<!DOCTYPE html>
<html lang="en">
<head>
<meta charset="utf-8">
<title>Pine Ridge Canine Coaching – Business Card</title>
<link href="https://fonts.googleapis.com/css2?family=Oswald:wght@500;600&family=Cormorant+Garamond:wght@500;600&display=swap" rel="stylesheet">
<style>
  :root {
    --backdrop: #565656;
    --card: #ffffff;
    --ink: #1b1b1b;
    --brand-blue: #0b33b0;
    --on-blue: #ffffff;
    --illustration-dark: #161616;
    --illustration-mid: #3a3a3a;
  }
  * { box-sizing: border-box; margin: 0; padding: 0; }
  html, body {
    width: 1200px;
    height: 1000px;
    overflow: hidden;
    background: var(--backdrop);
  }
  .canvas {
    position: relative;
    width: 1200px;
    height: 1000px;
  }
  .card {
    position: absolute;
    top: 185px;
    width: 360px;
    height: 630px;
    background: var(--card);
    overflow: hidden;
    box-shadow: 0 6px 18px rgba(0,0,0,0.35);
  }
  /* Front side */
  .card--front { left: 200px; }
  .front__portrait {
    position: absolute;
    left: 0;
    top: 0;
    width: 200px;
    height: 630px;
    background: linear-gradient(180deg, #ffffff 0%, var(--illustration-mid) 22%, var(--illustration-dark) 60%);
  }
  .front__name {
    position: absolute;
    left: 214px;
    top: 32px;
    height: 566px;
    writing-mode: vertical-rl;
    transform: rotate(180deg);
    font-family: "Oswald", sans-serif;
    font-weight: 600;
    font-size: 64px;
    line-height: 1;
    letter-spacing: 1px;
    text-transform: uppercase;
    color: var(--brand-blue);
    text-align: left;
    white-space: nowrap;
  }
  .front__title {
    position: absolute;
    left: 292px;
    top: 318px;
    height: 280px;
    writing-mode: vertical-rl;
    transform: rotate(180deg);
    font-family: "Cormorant Garamond", serif;
    font-weight: 500;
    font-size: 28px;
    line-height: 1.1;
    letter-spacing: 3px;
    text-transform: uppercase;
    color: var(--ink);
    text-align: left;
    white-space: nowrap;
  }
  /* Back side */
  .card--back { left: 640px; }
  .back__brand {
    position: absolute;
    left: 0;
    right: 0;
    top: 150px;
    height: 290px;
    display: flex;
    align-items: center;
    justify-content: center;
    text-align: center;
    font-family: "Oswald", sans-serif;
    font-weight: 600;
    font-size: 46px;
    line-height: 1.15;
    text-transform: uppercase;
    color: var(--ink);
    padding: 0 30px;
  }
  .back__contact-band {
    position: absolute;
    left: 0;
    right: 0;
    bottom: 0;
    height: 118px;
    background: var(--brand-blue);
    padding: 20px 22px 0;
    font-family: "Cormorant Garamond", serif;
    font-weight: 600;
    font-size: 15px;
    color: var(--on-blue);
  }
  .contact-row {
    display: flex;
    gap: 18px;
    margin-bottom: 14px;
  }
  .contact-row--center { justify-content: center; }
  .contact-item {
    display: flex;
    align-items: center;
    gap: 8px;
    white-space: nowrap;
  }
  .contact-icon {
    width: 18px;
    height: 18px;
    flex: none;
  }
</style>
</head>
<body>
<main class="canvas">

  <section class="card card--front" aria-label="Business card front">
    <div class="front__portrait" role="img" aria-label="Black and white illustration of a Doberman wearing a chain collar with a paw tag"></div>
    <h1 class="front__name">Trevor Holloway</h1>
    <p class="front__title">Dog Trainer</p>
  </section>

  <section class="card card--back" aria-label="Business card back">
    <div class="back__brand">Pine Ridge Canine Coaching</div>
    <div class="back__contact-band">
      <div class="contact-row">
        <span class="contact-item">
          <svg class="contact-icon" viewBox="0 0 18 18" aria-hidden="true">
            <rect x="0" y="0" width="18" height="18" rx="3" fill="#ffffff"/>
            <path d="M5 4 L7.5 4 L8.3 6.8 L7 8 Q8 10.5 10 11.2 L11.2 10 L14 10.8 L14 13.3 Q9.5 14.5 6.5 11.5 Q3.6 8.5 5 4 Z" fill="#0b33b0"/>
          </svg>
          555-304-7162
        </span>
        <span class="contact-item">
          <svg class="contact-icon" viewBox="0 0 18 18" aria-hidden="true">
            <rect x="0" y="0" width="18" height="18" rx="3" fill="#ffffff"/>
            <circle cx="9" cy="9" r="2.6" fill="none" stroke="#0b33b0" stroke-width="1.6"/>
            <path d="M11.6 9 V10.4 Q11.6 12 13 12 Q14.4 12 14.4 9 A5.4 5.4 0 1 0 11.5 13.8" fill="none" stroke="#0b33b0" stroke-width="1.6"/>
          </svg>
          info@pineridgecanine.example
        </span>
      </div>
      <div class="contact-row contact-row--center">
        <span class="contact-item">
          <svg class="contact-icon" viewBox="0 0 18 18" aria-hidden="true">
            <rect x="0" y="0" width="18" height="18" rx="3" fill="#ffffff"/>
            <circle cx="9" cy="9" r="5" fill="none" stroke="#0b33b0" stroke-width="1.4"/>
            <ellipse cx="9" cy="9" rx="2.2" ry="5" fill="none" stroke="#0b33b0" stroke-width="1.2"/>
            <line x1="4" y1="9" x2="14" y2="9" stroke="#0b33b0" stroke-width="1.2"/>
          </svg>
          www.pineridgecanine.example
        </span>
      </div>
    </div>
  </section>

</main>
</body>
</html>
```